Etiketten für Imkerei aus der Steiermark
Zielgruppe
Wir sind eine Imkerei aus der Steiermark / Österreich im Vollerwerb. www.talmann-biene.at
Zielgruppe: Frauen, Familien, Regional
Unser Image: hohe Qualität, Familienbetrieb, naturnah, gesund
Vermarktung: Direkt, Verkaufsstellen, Märkte, zukünftig auch online
Aufgabenstellung
Wir werden die Honiggläser und die Druckerei umstellen und möchten hierfür ein profesionelles abgestimmtes Design. Unser Logo soll erhalten bleiben. Die Honigsortenbezeichnung (Waldhonig, Cremehonig, Blütenhonig) soll zukünftig eingedruckt werden und neben dem Logo ein Zentrales Element sein.
In Zukunft verwenden wir Vintra Gläser mit hohen Deckel der Firma Glasoria in den Größen 1000g(Lise 785), 500g (Vin 410), 250 g (Vin 212) und 150 g (Vin 125). Der Deckel soll einheitlich Gold oder Silber sein.

```html
<!DOCTYPE html>
<html lang="de">
<head>
<meta charset="utf-8">
<title>Talmannbiene – Etiketten Waldhonig</title>
<link rel="stylesheet" href="https://fonts.googleapis.com/css2?family=Libre+Baskerville:wght@400;700&display=swap">
<style>
  :root {
    --green: #037a32;
    --olive: #857550;
    --olive-text: #7a6a44;
    --white: #ffffff;
    --honey: #f4e15a;
    --page: #ffffff;
  }
  * { box-sizing: border-box; margin: 0; padding: 0; }
  html, body {
    width: 1200px; height: 979px; overflow: hidden;
    background: var(--page);
    font-family: "Libre Baskerville", Georgia, serif;
  }
  .canvas { position: relative; width: 1200px; height: 979px; }

  .label {
    position: absolute; left: 335px;
    width: 530px; height: 162px;
    border: 5px solid var(--green);
    background: var(--white);
    color: var(--olive-text);
    box-shadow: 0 18px 30px rgba(0,0,0,0.22);
    overflow: hidden;
  }
  .label--light { top: 264px; }
  .label--dark  { top: 514px; background: var(--olive); color: var(--white); }
  .label--dark::after {
    content: ""; position: absolute; inset: 1px;
    border: 1px solid rgba(255,255,255,0.55); pointer-events: none;
  }

  .honeycomb-area {
    position: absolute; left: 106px; top: 0; width: 300px; height: 100%;
    background: radial-gradient(ellipse at center, rgba(200,190,160,0.35) 0%, rgba(200,190,160,0.12) 55%, rgba(200,190,160,0) 80%);
  }
  .label--dark .honeycomb-area {
    background: radial-gradient(ellipse at center, rgba(255,245,210,0.18) 0%, rgba(255,245,210,0.07) 55%, rgba(255,245,210,0) 80%);
  }

  .weight {
    position: absolute; left: 18px; top: 10px;
    font-size: 8px; letter-spacing: 2px;
  }
  .variety {
    position: absolute; left: 9px; top: 64px;
    display: inline-block; height: 24px;
    background: var(--green); color: var(--white);
    font-size: 16px; font-weight: 400; letter-spacing: 2.6px; line-height: 24px;
    padding: 0 4px 0 6px; white-space: nowrap;
  }
  .storage {
    position: absolute; left: 13px; top: 97px;
    font-size: 4.3px; font-weight: 700; letter-spacing: 0.5px; line-height: 6px;
    text-transform: uppercase;
  }

  .brand {
    position: absolute; left: 264px; top: 50px; transform: translateX(-50%);
    height: 54px; white-space: nowrap;
    display: flex; align-items: center; justify-content: center; gap: 6px;
  }
  .brand__dot {
    width: 14px; height: 14px; border-radius: 50%; background: var(--honey);
  }
  .brand__name {
    font-size: 15px; font-weight: 700; color: var(--olive-text);
  }
  .label--dark .brand__name { color: var(--white); }

  .quality {
    position: absolute; left: 264px; top: 130px; transform: translateX(-50%);
    display: inline-block; height: 12px; padding: 0 5px;
    border: 1px solid rgba(160,145,110,0.6);
    font-size: 6px; letter-spacing: 1.1px; line-height: 10px; text-align: center;
    white-space: nowrap;
  }
  .label--dark .quality { border-color: rgba(255,255,255,0.6); }

  .producer {
    position: absolute; right: 11px; top: 50px; text-align: right;
  }
  .producer__name { font-size: 6.6px; letter-spacing: 1.4px; margin-bottom: 6px; }
  .producer__contact {
    font-style: normal; font-size: 4.8px; letter-spacing: 0.8px; line-height: 7.4px;
    text-transform: uppercase;
  }
</style>
</head>
<body>
<main class="canvas">

  <section class="label label--light">
    <div class="honeycomb-area" role="img" aria-label="Dezentes Wabenmuster im Hintergrund"></div>
    <div class="weight">1000 G</div>
    <h1 class="variety">WALDHONIG</h1>
    <p class="storage">Trocken und vor Wärme geschützt lagern.<br>Mindestens haltbar bis:</p>
    <div class="brand"><span class="brand__dot"></span><span class="brand__name">Talmannbiene</span></div>
    <div class="quality">ÖSTERREICHISCHER QUALITÄTSHONIG</div>
    <div class="producer">
      <p class="producer__name">MEISTERIMKEREI TALMANN</p>
      <address class="producer__contact">
        Theresa &amp; Lukas<br>Almweg 12<br>8120 Talbach<br>T. 0660 / 31 47 205<br>post@talmann-biene.at<br>www.talmann-biene.at
      </address>
    </div>
  </section>

  <section class="label label--dark">
    <div class="honeycomb-area" role="img" aria-label="Dezentes Wabenmuster im Hintergrund"></div>
    <div class="weight">1000 G</div>
    <h2 class="variety">WALDHONIG</h2>
    <p class="storage">Trocken und vor Wärme geschützt lagern.<br>Mindestens haltbar bis:</p>
    <div class="brand"><span class="brand__dot"></span><span class="brand__name">Talmannbiene</span></div>
    <div class="quality">ÖSTERREICHISCHER QUALITÄTSHONIG</div>
    <div class="producer">
      <p class="producer__name">MEISTERIMKEREI TALMANN</p>
      <address class="producer__contact">
        Theresa &amp; Lukas<br>Almweg 12<br>8120 Talbach<br>T. 0660 / 31 47 205<br>post@talmann-biene.at<br>www.talmann-biene.at
      </address>
    </div>
  </section>

</main>
</body>
</html>
```